Business Card Design Project

I need a cool business card design for the company that will build residential houses.
The card should include:
1) Name: Boris Kalinov
2) Cell: 587.204.XXXX
3) Email: bor.kalinov@qwvend.example
4) Position: General Manager
5) Residential Home Building
6) Company logo that I have uploaded

Industry/Entity Type

Residential

```html
<!DOCTYPE html>
<html lang="en">
<head>
<meta charset="utf-8">
<title>Business Card – Boris Kalinov</title>
<link rel="stylesheet" href="https://fonts.googleapis.com/css2?family=Tinos&display=swap">
<style>
  :root {
    --paper: #ffffff;
    --brand-blue: #0d56a6;
    --brand-green: #8cc63f;
    --ink: #111111;
    --divider: #000000;
  }
  html, body {
    margin: 0;
    padding: 0;
    overflow: hidden;
  }
  body {
    width: 1200px;
    height: 1000px;
    background: var(--paper);
    font-family: "Tinos", "Times New Roman", serif;
  }
  .card {
    position: relative;
    width: 1200px;
    height: 1000px;
    background: var(--paper);
  }
  .tagline {
    position: absolute;
    top: 176px;
    left: 0;
    width: 1250px;
    margin: 0;
    text-align: center;
    font-size: 51px;
    font-weight: 400;
    color: var(--brand-blue);
    text-shadow: 3px 8px 8px rgba(0, 0, 0, 0.35);
    letter-spacing: 0.5px;
  }
  .company {
    position: absolute;
    left: 140px;
    top: 305px;
    width: 420px;
    height: 360px;
    display: flex;
    align-items: center;
    justify-content: center;
    gap: 16px;
  }
  .company-dot {
    width: 30px;
    height: 30px;
    border-radius: 50%;
    background: var(--brand-blue);
    flex: none;
  }
  .company-name {
    font-size: 38px;
    color: var(--brand-blue);
    line-height: 1.1;
  }
  .divider {
    position: absolute;
    left: 578px;
    top: 300px;
    width: 4px;
    height: 363px;
    background: var(--divider);
  }
  .contact {
    position: absolute;
    left: 600px;
    top: 360px;
  }
  .person-name {
    margin: 0;
    font-size: 50px;
    font-weight: 400;
    color: var(--brand-green);
    line-height: 1.1;
  }
  .person-role {
    margin: 2px 0 0;
    font-size: 30px;
    color: var(--ink);
  }
  .contact-list {
    list-style: none;
    margin: 44px 0 0;
    padding: 0;
    font-size: 30px;
    color: var(--ink);
  }
  .contact-list li {
    display: flex;
    align-items: center;
    gap: 6px;
    height: 40px;
  }
  .contact-icon {
    width: 28px;
    height: 28px;
    flex: none;
  }
</style>
</head>
<body>
  <main class="card">
    <h1 class="tagline">Residential Home Building</h1>

    <div class="company">
      <span class="company-dot"></span>
      <span class="company-name">Vellmar Developments</span>
    </div>

    <div class="divider"></div>

    <section class="contact">
      <h2 class="person-name">Boris Kalinov</h2>
      <p class="person-role">General Manager</p>
      <ul class="contact-list">
        <li>
          <svg class="contact-icon" viewBox="0 0 28 28" aria-hidden="true">
            <rect x="8" y="2" width="12" height="24" rx="2" fill="none" stroke="#111" stroke-width="2"/>
            <rect x="10" y="5" width="8" height="9" fill="#111"/>
            <circle cx="14" cy="20" r="2" fill="#111"/>
          </svg>
          <span>587.204.XXXX</span>
        </li>
        <li>
          <svg class="contact-icon" viewBox="0 0 28 28" aria-hidden="true">
            <path d="M3 11 L14 4 L25 11 V24 H3 Z" fill="none" stroke="#111" stroke-width="2" stroke-linejoin="round"/>
            <path d="M3 11 L14 18 L25 11 M3 24 L11 16 M25 24 L17 16" fill="none" stroke="#111" stroke-width="2"/>
          </svg>
          <span>bor.kalinov@qwvend.example</span>
        </li>
      </ul>
    </section>
  </main>
</body>
</html>
```